Australian IT Company New Logo Business Cards Required

We are a computer consultancy / MSP located in Brisbane Australia looking to have business cards designed with our new logo, we are looking for something professional that catches the eye.
I can provide the logo in other formats if required, let's see what you can create!

```html
<!DOCTYPE html>
<html lang="en">
<head>
<meta charset="utf-8">
<title>Velcora Business Cards</title>
<link href="https://fonts.googleapis.com/css2?family=Lato:wght@400;700;900&display=swap" rel="stylesheet">
<style>
  :root {
    --brand-green: #8cc63f;
    --ink-grey: #6b6b6b;
    --paper: #ffffff;
    --backdrop: #d3d3cf;
  }
  * { margin: 0; padding: 0; box-sizing: border-box; }
  html, body {
    width: 1200px;
    height: 801px;
    overflow: hidden;
    background: var(--backdrop);
    font-family: "Lato", sans-serif;
  }
  .canvas {
    position: relative;
    width: 1200px;
    height: 801px;
  }
  .card {
    position: absolute;
    top: 250px;
    width: 520px;
    height: 300px;
    box-shadow: 0 10px 24px rgba(0,0,0,0.18);
  }
  .card--front {
    left: 50px;
    background: var(--paper);
    border-bottom: 4px solid var(--brand-green);
  }
  .card--back {
    left: 630px;
    background: var(--brand-green);
  }

  /* Wordmark */
  .wordmark {
    position: absolute;
    display: flex;
    flex-direction: column;
    align-items: flex-start;
  }
  .wordmark__row {
    display: flex;
    align-items: center;
    gap: 8px;
  }
  .wordmark__dot {
    border-radius: 50%;
  }
  .wordmark__name {
    font-weight: 900;
    line-height: 1;
    letter-spacing: 0.02em;
  }
  .wordmark__tagline {
    font-weight: 700;
    letter-spacing: 0.08em;
    text-transform: uppercase;
  }

  .card--front .wordmark { left: 250px; top: 34px; }
  .card--front .wordmark__dot { width: 16px; height: 16px; background: var(--brand-green); }
  .card--front .wordmark__name { font-size: 40px; color: var(--brand-green); }
  .card--front .wordmark__tagline { font-size: 10.5px; color: var(--ink-grey); margin-top: 4px; }

  .card--back .wordmark { left: 80px; top: 100px; }
  .card--back .wordmark__dot { width: 30px; height: 30px; background: var(--paper); }
  .card--back .wordmark__name { font-size: 64px; color: var(--paper); }
  .card--back .wordmark__tagline { font-size: 16px; color: var(--paper); margin-top: 6px; }

  /* Front details */
  .divider {
    position: absolute;
    left: 22px;
    right: 22px;
    top: 176px;
    height: 1px;
    background: var(--brand-green);
  }
  .person {
    position: absolute;
    left: 26px;
    top: 112px;
  }
  .person__name {
    font-weight: 900;
    font-size: 22px;
    color: var(--brand-green);
    letter-spacing: 0.02em;
  }
  .person__role {
    font-size: 14px;
    color: var(--ink-grey);
    margin-top: 2px;
  }
  .contacts {
    position: absolute;
    left: 26px;
    top: 196px;
    list-style: none;
  }
  .contacts__item {
    display: flex;
    align-items: center;
    gap: 12px;
    font-size: 14px;
    color: var(--ink-grey);
    height: 26px;
  }
  .contacts__icon {
    width: 14px;
    height: 14px;
    flex: none;
  }
  .address {
    position: absolute;
    right: 26px;
    top: 196px;
    text-align: right;
    font-size: 14px;
    line-height: 24px;
    color: var(--ink-grey);
  }
</style>
</head>
<body>
<main class="canvas">

  <section class="card card--front" aria-label="Business card front">
    <div class="wordmark">
      <div class="wordmark__row">
        <span class="wordmark__dot"></span>
        <span class="wordmark__name">VELCORA</span>
      </div>
      <span class="wordmark__tagline">IT Solutions for Small Business</span>
    </div>

    <div class="person">
      <p class="person__name">JOHN SMITH</p>
      <p class="person__role">Founder &amp; CEO</p>
    </div>

    <div class="divider"></div>

    <ul class="contacts">
      <li class="contacts__item">
        <svg class="contacts__icon" viewBox="0 0 24 24" aria-hidden="true">
          <path fill="#8cc63f" d="M6.6 10.8a15.1 15.1 0 0 0 6.6 6.6l2.2-2.2a1 1 0 0 1 1-.25 11.4 11.4 0 0 0 3.6.57 1 1 0 0 1 1 1V20a1 1 0 0 1-1 1A17 17 0 0 1 3 4a1 1 0 0 1 1-1h3.5a1 1 0 0 1 1 1c0 1.25.2 2.45.57 3.57a1 1 0 0 1-.25 1z"/>
        </svg>
        1234567890
      </li>
      <li class="contacts__item">
        <svg class="contacts__icon" viewBox="0 0 24 24" aria-hidden="true">
          <rect x="2" y="5" width="20" height="14" rx="1" fill="#8cc63f"/>
          <path d="M2.5 6l9.5 7 9.5-7" fill="none" stroke="#fff" stroke-width="1.6"/>
        </svg>
        info@yourmail.com
      </li>
      <li class="contacts__item">
        <svg class="contacts__icon" viewBox="0 0 24 24" aria-hidden="true">
          <circle cx="12" cy="12" r="10" fill="#8cc63f"/>
          <g fill="none" stroke="#fff" stroke-width="1.3">
            <ellipse cx="12" cy="12" rx="4" ry="9"/>
            <path d="M3 12h18M5 7.5h14M5 16.5h14"/>
          </g>
        </svg>
        www.yourwebsite.com
      </li>
    </ul>

    <address class="address">
      1234 First Line Address<br>
      5678 Second Line Address
    </address>
  </section>

  <section class="card card--back" aria-label="Business card back">
    <div class="wordmark">
      <div class="wordmark__row">
        <span class="wordmark__dot"></span>
        <span class="wordmark__name">VELCORA</span>
      </div>
      <span class="wordmark__tagline">IT Solutions for Small Business</span>
    </div>
  </section>

</main>
</body>
</html>
```